Mental Health

KVR HAVEN
Behavioral Health
4172 E. Dorrel St. Mesa, AZ 85217
Marguerite (480)555-0142 / Ivan 480-555-0187

Email: KVRHaven@Qortamail.com
Newly Remodeled & Spacious
g Staff
Registered Nurses
Licensed Independent &
Professional Substance &
Abuse Counselors
Behavioral Health Techs
Certified Caregivers
Behavioral Health &
Substance Abuse Professionals

To Refer a Patient
About Us
KVR Haven is a Fully Staffed Behavioral
Health Residential Facility, providing
treatment plans for adults suffering
with various Behavioral Health and
Substance Abuse disorders, while living
in a nice safe, clean and supportive
environment. Our home offers clients the
ability to learn the necessary skills to
help clients adapt, build self confidence
as well as independence, with the goal
of reducing the probability of a future
crisis or possible relapse. We offer
counseling programs, consisting of a
variety of addiction and recovery support
groups, independent living, coping and
social skills groups, as well as assisting
clients with using tools to create a resume
to help obtain employment and so much
more. We are committed to teaching
self management care and allowing
clients to understand how to utilize the
resources, skills and tools available for
long term success by providing superior
quality, all-inclusive living arrangements
and treatment options.

Thank you for your patience while I update the final content needed for us to make the final decision this week.

```html
<!DOCTYPE html>
<html lang="en">
<head>
<meta charset="utf-8">
<title>KVR Haven – Business Card</title>
<link rel="stylesheet" href="https://fonts.googleapis.com/css2?family=Poppins:wght@400;500;600&display=swap">
<style>
  :root {
    --bg: #2a2a2c;
    --white: #ffffff;
    --blue: #1a6cc4;
    --blue-deep: #1d5fb8;
    --purple: #5b3fa0;
    --pink: #e8479a;
    --green: #7cb342;
    --yellow: #f0b429;
    --red: #d32f2f;
    --ink: #2d3a4a;
  }
  * { box-sizing: border-box; margin: 0; padding: 0; }
  html, body { width: 1200px; height: 900px; overflow: hidden; }
  body {
    background: var(--bg);
    font-family: "Poppins", sans-serif;
    display: flex;
    flex-direction: column;
    align-items: center;
    justify-content: center;
    gap: 30px;
  }
  .card {
    position: relative;
    width: 700px;
    height: 400px;
    border-radius: 22px;
    overflow: hidden;
  }

  /* Front */
  .card-front {
    background:
      radial-gradient(circle at 0% 100%, var(--yellow) 0%, rgba(240,180,41,0) 45%),
      radial-gradient(circle at 100% 0%, var(--purple) 0%, rgba(91,63,160,0) 55%),
      linear-gradient(100deg, var(--pink) 0%, #8a9a7a 35%, #3f8f90 60%, #3a6cb0 100%);
    display: flex;
    align-items: center;
    justify-content: center;
  }
  .brand {
    display: flex;
    align-items: center;
    gap: 18px;
  }
  .brand-dot {
    width: 70px; height: 70px;
    border-radius: 50%;
    background: var(--white);
  }
  .brand-name {
    font-weight: 500;
    font-size: 54px;
    letter-spacing: 4px;
    color: var(--white);
  }

  /* Back */
  .card-back { background: var(--white); }
  .back-shapes { position: absolute; inset: 0; }
  .back-brand {
    position: absolute;
    top: 34px; right: 70px;
    display: flex; align-items: center; gap: 12px;
  }
  .back-brand .brand-dot { width: 48px; height: 48px; background: var(--blue); }
  .back-brand .brand-name { font-size: 36px; color: var(--blue); letter-spacing: 3px; }

  .contacts {
    position: absolute;
    top: 70px; left: 36px;
    display: flex; align-items: flex-start; gap: 16px;
  }
  .contact { display: flex; flex-direction: column; gap: 2px; }
  .contact-name {
    font-weight: 600; font-size: 17px; color: var(--blue);
    text-transform: uppercase; letter-spacing: 1px;
  }
  .contact-phone {
    display: flex; align-items: center; gap: 7px;
    font-size: 15px; color: var(--red); font-weight: 500;
  }
  .icon-badge {
    width: 20px; height: 20px; border-radius: 50%;
    background: var(--green);
    display: inline-flex; align-items: center; justify-content: center;
    flex: none;
  }
  .divider { width: 2px; height: 48px; background: var(--pink); margin-top: 6px; }

  .services {
    position: absolute;
    top: 150px; left: 36px;
    list-style: none;
    font-size: 13.5px; line-height: 20px; color: var(--ink);
  }
  .services li { display: flex; align-items: flex-start; gap: 10px; }
  .leaf {
    width: 9px; height: 14px; margin-top: 4px;
    border-radius: 0 9px 0 9px;
    transform: rotate(30deg);
    flex: none;
  }
  .leaf.blue { background: var(--blue); }
  .leaf.pink { background: var(--pink); }
  .leaf.red { background: var(--red); }
  .leaf.green { background: var(--green); }
  .leaf.yellow { background: var(--yellow); }
  .leaf.none { visibility: hidden; }

  .details {
    position: absolute;
    right: 40px; bottom: 70px;
    text-align: right;
    color: var(--white);
    font-size: 15px; line-height: 24px;
  }
  .details p { display: flex; align-items: center; justify-content: flex-end; gap: 10px; }
</style>
</head>
<body>

  <section class="card card-front">
    <div class="brand">
      <span class="brand-dot"></span>
      <span class="brand-name">KVR HAVEN</span>
    </div>
  </section>

  <section class="card card-back">
    <svg class="back-shapes" viewBox="0 0 700 400" width="700" height="400" aria-hidden="true">
      <defs>
        <linearGradient id="blueField" x1="0" y1="1" x2="1" y2="0">
          <stop offset="0" stop-color="#1a6cc4"/>
          <stop offset="0.7" stop-color="#2b63bd"/>
          <stop offset="1" stop-color="#5b3fa0"/>
        </linearGradient>
      </defs>
      <path d="M0 345 C220 310 380 320 500 200 C570 130 640 105 700 100 L700 400 L0 400 Z" fill="url(#blueField)"/>
      <path d="M0 318 C170 300 300 320 420 230 C470 190 500 160 520 145 C490 200 420 270 300 300 C200 325 90 320 0 335 Z" fill="var(--green)"/>
      <path d="M170 355 C360 330 450 210 560 120 C610 82 660 66 700 60" fill="none" stroke="var(--pink)" stroke-width="7" stroke-linecap="round"/>
    </svg>

    <div class="back-brand">
      <span class="brand-dot"></span>
      <span class="brand-name">KVR HAVEN</span>
    </div>

    <div class="contacts">
      <div class="contact">
        <span class="contact-name">Marguerite</span>
        <span class="contact-phone">
          <span class="icon-badge">
            <svg width="11" height="11" viewBox="0 0 24 24"><path fill="#fff" d="M6.6 10.8a15 15 0 0 0 6.6 6.6l2.2-2.2c.3-.3.7-.4 1-.2 1.1.4 2.3.6 3.6.6.6 0 1 .4 1 1V20c0 .6-.4 1-1 1A17 17 0 0 1 3 4c0-.6.4-1 1-1h3.5c.6 0 1 .4 1 1 0 1.3.2 2.5.6 3.6.1.3 0 .7-.2 1z"/></svg>
          </span>
          (480)555-0142
        </span>
      </div>
      <span class="divider"></span>
      <div class="contact">
        <span class="contact-name">Ivan</span>
        <span class="contact-phone">
          <span class="icon-badge">
            <svg width="11" height="11" viewBox="0 0 24 24"><path fill="#fff" d="M6.6 10.8a15 15 0 0 0 6.6 6.6l2.2-2.2c.3-.3.7-.4 1-.2 1.1.4 2.3.6 3.6.6.6 0 1 .4 1 1V20c0 .6-.4 1-1 1A17 17 0 0 1 3 4c0-.6.4-1 1-1h3.5c.6 0 1 .4 1 1 0 1.3.2 2.5.6 3.6.1.3 0 .7-.2 1z"/></svg>
          </span>
          480-555-0187
        </span>
      </div>
    </div>

    <ul class="services">
      <li><span class="leaf blue"></span>Newly Remodeled &amp; Spacious g Staff</li>
      <li><span class="leaf pink"></span>Registered Nurses</li>
      <li><span class="leaf red"></span>Licensed Independent &amp; Professional</li>
      <li><span class="leaf none"></span>Substance &amp; Abuse Counselors</li>
      <li><span class="leaf green"></span>Behavioral Health Techs Certified Caregivers</li>
      <li><span class="leaf yellow"></span>Behavioral Health &amp; Substance Abuse</li>
      <li><span class="leaf none"></span>Professionals</li>
    </ul>

    <div class="details">
      <p>KVRHaven@Qortamail.com
        <span class="icon-badge">
          <svg width="11" height="11" viewBox="0 0 24 24"><path fill="#fff" d="M3 5h18v14H3z M3 5l9 7 9-7" stroke="#7cb342" stroke-width="1.5"/></svg>
        </span>
      </p>
      <p>Behavioral Health
        <span class="icon-badge">
          <svg width="11" height="11" viewBox="0 0 24 24"><path fill="#fff" d="M12 2a7 7 0 0 0-7 7c0 5 7 13 7 13s7-8 7-13a7 7 0 0 0-7-7zm0 9.5A2.5 2.5 0 1 1 12 6.5a2.5 2.5 0 0 1 0 5z"/></svg>
        </span>
      </p>
      <p>4172 E. Dorrel St. Mesa, AZ 85217</p>
    </div>
  </section>

</body>
</html>
```